hotel's Website

Hotels website redesign for reference pictures, logo etc see http://restwellharbourside.co.uk/

1. 2-3 Special offers on the main page.
2. Booking calender
3. Location Map
4. Picture gallery.
5. Journeyrater reviews.
6. short description
7. Social Media sharing.
8 Phone number and address.

Industry/Entity Type

Hotel

Requirements
Must have
• 1. 2-3 Special offers on the main page.
2. Booking calender
3. Location Map
4. Picture gallery.
5. Journeyrater reviews.
6. short description
7. Social Media sharing.

```html
<!DOCTYPE html>
<html lang="en">
<head>
<meta charset="utf-8">
<title>Restwell Harbourside – Hotel</title>
<link rel="stylesheet" href="https://fonts.googleapis.com/css2?family=Open+Sans:wght@300;400;600;700&family=Noto+Serif:wght@400;700&display=swap">
<style>
:root{
  --orange:#e8481f;
  --orange-dark:#b8330f;
  --navy:#1c0f4a;
  --plum:#2a1a3a;
  --paper:#f1eee8;
  --gallery-bg:#e3e1e0;
  --green:#4f8a62;
  --ink:#333;
  --muted:#777;
  --footer:#232323;
  --footer-dark:#171717;
  --white:#fff;
}
*{box-sizing:border-box;margin:0;padding:0}
html,body{width:1200px;height:2824px;overflow:hidden}
body{position:relative;background:var(--paper);font-family:"Open Sans",Arial,sans-serif;color:var(--ink)}
.abs{position:absolute}
.photo{position:absolute}

/* top bar */
.topbar{left:0;top:0;width:1200px;height:30px;background:#2b1f3b;color:#eee;font-size:11px}
.topbar .contact{position:absolute;top:0;height:30px;display:flex;align-items:center;gap:8px}
.topbar .ico{width:20px;height:20px;background:#4a3d5a;display:flex;align-items:center;justify-content:center}
.topbar .social{position:absolute;left:762px;top:8px;display:flex;gap:20px}
.dot{width:14px;height:14px;border-radius:50%;background:#d9d9e6}
.location-link{position:absolute;right:0;top:0;width:200px;height:30px;background:var(--navy);color:#fff;font-size:11px;display:flex;align-items:center;padding-left:10px;gap:10px}

/* hero */
.hero{left:0;top:0;width:1200px;height:350px;background:linear-gradient(110deg,#c9bdaa 0%,#e6ddd0 30%,#8a7b68 55%,#4a3e3a 75%,#a69683 100%)}
.nav{left:0;top:30px;width:1200px;height:66px;background:rgba(240,235,228,.72)}
.brand{position:absolute;left:256px;top:6px;height:56px;display:flex;align-items:center;gap:8px}
.brand .mark{width:14px;height:14px;background:var(--navy)}
.brand span{font-family:"Noto Serif",serif;font-weight:700;font-size:20px;color:var(--navy)}
.menu{position:absolute;left:334px;top:30px;display:flex;gap:24px;font-size:10.5px;font-weight:600;color:#3a2a3a;text-transform:uppercase}
.menu li{list-style:none}
.search{position:absolute;left:924px;top:28px}
.hero-title{left:260px;top:140px;width:310px;height:40px;background:var(--orange);color:#fff;font-size:27px;font-weight:400;padding-left:18px;line-height:40px}
.hero-sub{left:300px;top:190px;width:292px;height:22px;background:rgba(40,30,40,.55);color:#fff;font-size:14px;line-height:22px;padding-left:12px}
.hero-btn{left:454px;top:216px;width:126px;height:38px;background:var(--navy);color:#fff;font-size:20px;line-height:38px;text-align:center;border-bottom:3px solid #0b0624}
.arrow-side{top:145px;width:24px;height:46px;background:rgba(60,60,60,.55);display:flex;align-items:center;justify-content:center}

/* booking */
.booking{left:264px;top:386px;display:flex;gap:0}
.field{position:absolute;top:0;height:34px;background:var(--orange);color:#fff;font-size:11px;display:flex;align-items:center;padding-left:20px;box-shadow:0 2px 0 var(--orange-dark)}
.field .tail{position:absolute;right:0;top:0;width:36px;height:34px;background:#d63d16;display:flex;align-items:center;justify-content:center;border-left:1px solid #f07050}
.check{position:absolute;top:0;height:34px;background:var(--navy);color:#fff;font-size:11px;display:flex;align-items:center;justify-content:center;border:2px solid #fff;outline:1px solid var(--navy)}

/* offers */
.offer{position:absolute;top:460px;width:194px;text-align:center}
.offer .photo{position:relative;width:194px;height:172px;border:5px solid #fff;box-shadow:0 2px 6px rgba(0,0,0,.3)}
.offer h3{font-family:"Noto Serif",serif;font-weight:700;color:var(--green);font-size:17px;line-height:20px;margin-top:18px}
.offer p{font-size:11px;line-height:15px;color:#444;margin:8px 14px 0;height:30px}
.offer .btn{display:inline-flex;align-items:center;gap:10px;margin-top:6px;background:var(--orange);color:#fff;font-size:15px;font-weight:700;height:32px;padding:0 14px 0 8px;box-shadow:0 2px 0 var(--orange-dark)}
.ext{width:18px;height:18px}

/* about band */
.about{left:0;top:788px;width:1200px;height:440px;background:linear-gradient(180deg,#2b1b26 0%,#4a3038 45%,#5b3a44 70%,#3a2630 100%)}
.about-text{left:266px;top:836px;width:670px;color:#fff;font-weight:300;font-size:23.5px;line-height:32px;letter-spacing:.4px}
.book-big{left:414px;top:1098px;width:334px;height:72px;background:var(--orange);border:3px solid #fff;outline:2px solid var(--orange);color:#fff;font-size:40px;font-weight:600;display:flex;align-items:center;justify-content:center;gap:16px;box-shadow:0 6px 0 #7a1e08}

/* reviews */
.rev-head{left:256px;top:1252px;width:688px;height:44px;background:var(--orange);color:#fff;font-family:"Noto Serif",serif;font-weight:700;font-size:20px;display:flex;align-items:center;gap:14px;padding-left:10px;letter-spacing:.5px}
.badge{width:32px;height:32px;border-radius:50%;background:#fff}
.review{left:268px;width:676px}
.review .stars{position:absolute;left:0;top:0;color:var(--orange);font-size:15px;letter-spacing:1px}
.review .name{position:absolute;left:76px;top:0;font-weight:700;font-size:16px;color:#222}
.review .date{position:absolute;left:76px;top:24px;font-size:10px;color:#777}
.review p{position:absolute;left:148px;top:20px;width:520px;font-size:11.5px;line-height:16px;color:#666}
.divider{left:256px;width:688px;height:1px;background:#cfcac2}
.viewall{left:740px;top:1472px;width:176px;height:36px;background:var(--navy);color:#fff;font-size:17px;display:flex;align-items:center;justify-content:center;gap:14px;border:2px solid #fff;outline:1px solid var(--navy)}
.viewall .badge{width:22px;height:22px}

/* events & videos */
.sec-tag{top:1538px;height:28px;background:var(--orange);color:#fff;font-family:"Noto Serif",serif;font-size:18px;line-height:28px;padding-left:8px;width:216px}
.event{left:256px;width:344px;height:112px;background:#dcd6cf}
.event .day{position:absolute;left:8px;top:8px;width:40px;height:36px;background:#fff;text-align:center;font-size:13px;line-height:22px}
.event .day b{display:block;background:var(--orange);color:#fff;font-size:10px;line-height:14px}
.event .thumb{position:absolute;left:56px;top:10px;width:66px;height:72px;border:3px solid #fff}
.event h4{position:absolute;left:132px;top:4px;font-size:13px;font-weight:400;color:#222}
.event .cm{position:absolute;left:132px;top:24px;font-size:9px;color:#888}
.event p{position:absolute;left:132px;top:40px;width:204px;font-size:9.5px;line-height:12px;color:#555}
.event .more{position:absolute;right:20px;bottom:6px;font-size:9.5px;color:#333}
.video{left:618px;top:1606px;width:326px;height:176px;background:linear-gradient(180deg,#0d1a33 0%,#1d2e5a 50%,#3a2a1c 100%)}
.video .title{position:absolute;left:8px;top:6px;color:#fff;font-size:14px}
.video .play{position:absolute;left:138px;top:72px;width:46px;height:32px;background:#3a3a3a;border-radius:6px;display:flex;align-items:center;justify-content:center}
.video .bar{position:absolute;left:0;bottom:0;width:326px;height:16px;background:#111}

/* gallery */
.gallery{left:0;top:1840px;width:1200px;height:634px;background:var(--gallery-bg)}
.gal-title{left:0;top:1870px;width:1200px;display:flex;justify-content:center;align-items:center;gap:14px;font-family:"Noto Serif",serif;font-weight:700;font-size:28px;letter-spacing:1px;color:#222}
.eye{width:26px;height:26px;border-radius:50%;background:var(--orange);display:flex;align-items:center;justify-content:center}
.gitem{position:absolute;width:220px;height:186px;background:#7b706b;border-radius:3px;overflow:hidden;box-shadow:0 1px 3px rgba(0,0,0,.3)}
.gitem .photo{position:relative;width:220px;height:144px}
.gitem h5{font-weight:400;color:#fff;font-size:15px;margin:4px 0 0 10px}
.gitem small{display:block;color:#e8e0dc;font-size:9.5px;margin-left:10px}

/* tweet band */
.tweet{left:0;top:2494px;width:1200px;height:64px;background:var(--orange);color:#fff;font-size:12px;display:flex;align-items:center;padding-left:264px;gap:28px}
.tweet .dot{width:30px;height:30px;background:#fff}

/* footer */
.footer{left:0;top:2570px;width:1200px;height:222px;background:var(--footer)}
.fcol{position:absolute;top:2606px;color:#ddd;font-size:11px;line-height:15px}
.fcol h6{font-family:"Noto Serif",serif;font-weight:400;font-size:13px;color:#fff;letter-spacing:.5px;margin-bottom:12px}
.fbtn{position:absolute;width:66px;height:24px;background:var(--navy);color:#fff;font-size:12px;display:flex;align-items:center;justify-content:center;gap:8px;border:1px solid #fff}
.thumbs{display:grid;grid-template-columns:repeat(3,42px);gap:10px 14px}
.thumbs div{height:42px;border:2px solid var(--orange)}
.blog li{list-style:none}
.bottom{left:0;top:2792px;width:1200px;height:32px;background:var(--footer-dark);color:#888;font-size:10px;padding-left:256px;line-height:32px}
.bottom .social{position:absolute;left:762px;top:11px;display:flex;gap:24px}
.bottom .dot{width:10px;height:10px;background:#777}
</style>
</head>
<body>

<!-- hero -->
<div class="abs hero" role="img" aria-label="Photo of a smiling couple on a scooter in front of white Georgian townhouses"></div>

<div class="abs topbar">
  <div class="contact" style="left:256px">
    <span class="ico"><svg width="12" height="12" viewBox="0 0 12 12"><path d="M2 1h3l1 3-2 1c1 2 2 3 3 3l1-2 3 1v3c-6 0-9-3-9-9z" fill="#fff"/></svg></span>
    <span>+44 (0) 20 7946 0123</span>
  </div>
  <div class="contact" style="left:398px">
    <span class="ico"><svg width="12" height="10" viewBox="0 0 12 10"><rect x="0.5" y="0.5" width="11" height="9" fill="none" stroke="#fff"/><path d="M1 1l5 4 5-4" fill="none" stroke="#fff"/></svg></span>
    <span>stay@restwellharbourside.co.uk</span>
  </div>
  <div class="social"><span class="dot"></span><span class="dot"></span><span class="dot"></span></div>
  <div class="location-link">Click Here To View Location
    <svg width="22" height="12" viewBox="0 0 22 12"><path d="M0 6h16M12 2l5 4-5 4" stroke="#fff" stroke-width="2" fill="none"/><circle cx="20" cy="6" r="2" fill="#fff"/></svg>
  </div>
</div>

<header class="abs nav">
  <div class="brand"><span class="mark"></span><span>Restwell</span></div>
  <ul class="menu">
    <li>Home</li><li>Bedrooms</li><li>Attractions</li><li>London Events</li><li>Special Offers</li><li>Photos</li><li>Videos</li><li>Contact</li>
  </ul>
  <svg class="search" width="14" height="14" viewBox="0 0 14 14"><circle cx="5.5" cy="5.5" r="4.2" fill="none" stroke="#3a2a3a" stroke-width="2"/><path d="M8.5 8.5l4.5 4.5" stroke="#3a2a3a" stroke-width="2.4"/></svg>
</header>

<div class="abs arrow-side" style="left:0"><svg width="10" height="16" viewBox="0 0 10 16"><path d="M8 1L2 8l6 7" stroke="#fff" stroke-width="2" fill="none"/></svg></div>
<div class="abs arrow-side" style="right:0"><svg width="10" height="16" viewBox="0 0 10 16"><path d="M2 1l6 7-6 7" stroke="#fff" stroke-width="2" fill="none"/></svg></div>

<div class="abs hero-title">Lorem ipsum dolor sit</div>
<div class="abs hero-sub">Sed ut perspiciatis unde omnis iste natus</div>
<div class="abs hero-btn">Click Here</div>

<!-- booking -->
<div class="abs booking" style="left:0;top:386px;width:1200px;height:40px">
  <div class="field" style="left:264px;width:116px">Arrive<span class="tail"><svg width="14" height="12" viewBox="0 0 14 12"><rect x="1" y="2" width="12" height="9" fill="none" stroke="#fff" stroke-width="1.5"/><path d="M1 5h12" stroke="#fff"/></svg></span></div>
  <div class="field" style="left:402px;width:114px">Depart<span class="tail"><svg width="14" height="12" viewBox="0 0 14 12"><rect x="1" y="2" width="12" height="9" fill="none" stroke="#fff" stroke-width="1.5"/><path d="M1 5h12" stroke="#fff"/></svg></span></div>
  <div class="field" style="left:544px;width:116px">Guests<span class="tail" style="width:30px"><span style="display:block;width:16px;height:12px;background:#fff;color:#333;font-size:9px;text-align:center;line-height:12px">1</span></span></div>
  <div class="field" style="left:678px;width:96px">Room<span class="tail" style="width:40px"><span style="display:block;width:28px;height:12px;background:#fff"></span></span></div>
  <div class="check" style="left:786px;width:152px">Check Availability</div>
</div>

<!-- offers -->
<div class="offer" style="left:256px">
  <div class="photo" role="img" aria-label="Sepia photo of a classical statue for the spa offer" style="background:linear-gradient(160deg,#b8ac6a,#6a5e2c)"></div>
  <h3>25% off on Spa<br>Treatments</h3>
  <p>Stay with us and get 25% off on Spa Treatments.</p>
  <span class="btn"><svg class="ext" viewBox="0 0 18 18"><rect x="2" y="5" width="11" height="11" fill="none" stroke="#fff" stroke-width="2"/><path d="M8 10l8-8M11 2h5v5" stroke="#fff" stroke-width="2" fill="none"/></svg>Get it</span>
</div>
<div class="offer" style="left:500px">
  <div class="photo" role="img" aria-label="Purple tinted photo of a busy London shopping street" style="background:linear-gradient(160deg,#8a6cc0,#3a2260)"></div>
  <h3>Shopping in<br>London</h3>
  <p>For the ultimate discount sales shopping London is always ...</p>
  <span class="btn"><svg class="ext" viewBox="0 0 18 18"><rect x="2" y="5" width="11" height="11" fill="none" stroke="#fff" stroke-width="2"/><path d="M8 10l8-8M11 2h5v5" stroke="#fff" stroke-width="2" fill="none"/></svg>Shop Now</span>
</div>
<div class="offer" style="left:748px">
  <div class="photo" role="img" aria-label="Sepia photo of a small hire car on a London street" style="background:linear-gradient(160deg,#c9c2a4,#7a7258)"></div>
  <h3>Low Cost<br>Car Hire</h3>
  <p>Driving in central London – Hire a car</p>
  <span class="btn"><svg class="ext" viewBox="0 0 18 18"><rect x="2" y="5" width="11" height="11" fill="none" stroke="#fff" stroke-width="2"/><path d="M8 10l8-8M11 2h5v5" stroke="#fff" stroke-width="2" fill="none"/></svg>Book Now</span>
</div>

<!-- about -->
<section class="abs about" role="img" aria-label="Dimly lit photo of a hotel bedroom with a double bed and bedside lamps"></section>
<p class="abs about-text">Our tastefully appointed four storey building is comprised of three attractive Georgian style townhouses – beautifully renovated and continuously maintained to provide comfort as well as stylish decor and useful amenities in all rooms. Our Hotel is a non smoking hotel</p>
<div class="abs book-big">Book Now
  <svg width="34" height="30" viewBox="0 0 34 30"><path d="M1 14L33 1 26 29 16 20 28 6 12 18z" fill="#fff"/></svg>
</div>

<!-- reviews -->
<div class="abs rev-head"><span class="badge"></span>SEE WHAT &nbsp;VISTORS ARE WRITING IN JOURNEYRATER</div>

<div class="abs review" style="top:1306px;height:70px">
  <span class="stars">★★★★</span>
  <span class="name" style="left:76px">John Doe</span>
  <span class="date">Nov 26, 2013</span>
  <p>Lorem ipsum dolor sit amet, consectetur adipisicing elit, sed do eiusmod tempor incididunt ut labore et dolore magna aliqua. Ut enim ad minim veniam, quis nostrud exercitation ullamco laboris nisi ut aliquip ex ea commodo consequat.</p>
</div>
<div class="abs divider" style="top:1394px"></div>
<div class="abs review" style="top:1414px;height:70px">
  <span class="stars">★★★★</span>
  <span class="name">John Doe</span>
  <span class="date">Nov 26, 2013</span>
  <p>Lorem ipsum dolor sit amet, consectetur adipisicing elit, sed do eiusmod tempor incididunt ut labore et dolore magna aliqua. Ut enim ad minim veniam, quis nostrud exercitation ullamco laboris nisi ut aliquip ex ea commodo consequat.</p>
</div>
<div class="abs divider" style="top:1460px;left:256px;width:470px"></div>
<div class="abs viewall">VIEW ALL <span class="badge"></span></div>

<!-- events -->
<div class="abs sec-tag" style="left:254px">LATEST EVENTS</div>
<div class="abs sec-tag" style="left:620px">LATEST VIDEOS</div>
<div class="abs" style="left:880px;top:1544px;font-size:11px;color:#333;display:flex;gap:6px;align-items:center">View all
  <svg width="12" height="10" viewBox="0 0 12 10"><path d="M1 9C2 4 5 3 9 3M7 1l3 2-3 2" stroke="#222" stroke-width="2" fill="none"/></svg></div>

<article class="abs event" style="top:1580px">
  <div class="day">01<b>NOV</b></div>
  <div class="thumb" role="img" aria-label="Photo of guards in red uniforms" style="background:linear-gradient(160deg,#3a3a5a,#b02a2a)"></div>
  <h4>Lorem ipsum dolor</h4>
  <span class="cm">10 Comments</span>
  <p>Neque porro quisquam est, qui dolorem ipsum quia dolor sit amet, consectetur, adipisci velit, sed quia non numquam eius modi tempora incidunt ut labore et dolore magnam aliquam</p>
  <span class="more">Read More ➦</span>
</article>
<article class="abs event" style="top:1704px">
  <div class="day">01<b>NOV</b></div>
  <div class="thumb" role="img" aria-label="Colourful photo of a street carnival" style="background:linear-gradient(160deg,#3a8ad0,#e0a030,#c02a6a)"></div>
  <h4>At vero eos et accusamus</h4>
  <span class="cm">8 Comments</span>
  <p>Neque porro quisquam est, qui dolorem ipsum quia dolor sit amet, consectetur, adipisci velit, sed quia non numquam eius modi tempora incidunt ut labore et dolore magnam aliquam</p>
  <span class="more">Read More ➦</span>
</article>

<div class="abs video" role="img" aria-label="Video still of a London ferris wheel lit up at night">
  <span class="title">2013 Restwell Harbourside London Event1</span>
  <span class="play"><svg width="14" height="16" viewBox="0 0 14 16"><path d="M1 1l12 7-12 7z" fill="#fff"/></svg></span>
  <span class="bar"></span>
</div>

<!-- gallery -->
<section class="abs gallery"></section>
<div class="abs gal-title"><span class="eye"><svg width="14" height="10" viewBox="0 0 14 10"><ellipse cx="7" cy="5" rx="6" ry="4" fill="none" stroke="#fff" stroke-width="1.6"/><circle cx="7" cy="5" r="1.8" fill="#fff"/></svg></span>GALLERY</div>

<div class="gitem" style="left:256px;top:1956px"><div class="photo" role="img" aria-label="Hotel bedroom with red bedspread" style="background:linear-gradient(160deg,#c9a040,#f0e6d6 55%,#a02a1a)"></div><h5>Lorem Ipsum</h5><small>Sed ut perspiciatis unde omnis</small></div>
<div class="gitem" style="left:490px;top:1956px"><div class="photo" role="img" aria-label="Hotel room with a desk and chairs" style="background:linear-gradient(160deg,#e6dcc0,#c8b896 60%,#8a6a3a)"></div><h5>Lorem Ipsum</h5><small>Sed ut perspiciatis unde omnis</small></div>
<div class="gitem" style="left:724px;top:1956px"><div class="photo" role="img" aria-label="Twin bedroom with patterned bedspreads" style="background:linear-gradient(160deg,#4a3a2a,#d0c4b0 50%,#9a3a1a)"></div><h5>Lorem Ipsum</h5><small>Sed ut perspiciatis unde omnis</small></div>
<div class="gitem" style="left:256px;top:2158px"><div class="photo" role="img" aria-label="Bright bedroom with yellow walls and white bed" style="background:linear-gradient(160deg,#d8c060,#f4f0e6 55%,#b8a040)"></div><h5>Lorem Ipsum</h5><small>Sed ut perspiciatis unde omnis</small></div>
<div class="gitem" style="left:490px;top:2158px"><div class="photo" role="img" aria-label="Hotel room with a desk and chairs" style="background:linear-gradient(160deg,#e6dcc0,#c8b896 60%,#8a6a3a)"></div><h5>Lorem Ipsum</h5><small>Sed ut perspiciatis unde omnis</small></div>
<div class="gitem" style="left:724px;top:2158px"><div class="photo" role="img" aria-label="Twin bedroom with patterned bedspreads" style="background:linear-gradient(160deg,#4a3a2a,#d0c4b0 50%,#9a3a1a)"></div><h5>Lorem Ipsum</h5><small>Sed ut perspiciatis unde omnis</small></div>

<!-- tweet band -->
<div class="abs tweet"><span class="dot"></span>Lorem ipsum dolor sit amet, consectetur adipisicing elit, sed do eiusmod tempor incididunt ut labore</div>

<!-- footer -->
<footer class="abs footer"></footer>
<div class="fcol" style="left:256px;width:170px">
  <h6>ABOUT US</h6>
  <p>Sed ut perspiciatis unde omnis iste natus error sit voluptatem accusantium doloremque laudantium, totam rem aperiam, eaque ipsa quae ab illo inventore veritatis et quasi.</p>
</div>
<div class="fbtn" style="left:350px;top:2754px">More <svg width="12" height="10" viewBox="0 0 12 10"><path d="M1 9C2 4 5 3 9 3M7 1l3 2-3 2" stroke="#fff" stroke-width="2" fill="none"/></svg></div>

<div class="fcol" style="left:442px">
  <h6>ATTRACTIONS</h6>
  <div class="thumbs">
    <div role="img" aria-label="Attraction photo" style="background:#c04a3a"></div>
    <div role="img" aria-label="Attraction photo" style="background:#3a4a8a"></div>
    <div role="img" aria-label="Attraction photo" style="background:#d0a040"></div>
    <div role="img" aria-label="Attraction photo" style="background:#b0603a"></div>
    <div role="img" aria-label="Attraction photo" style="background:#8a3a3a"></div>
    <div role="img" aria-label="Attraction photo" style="background:#4a7ab0"></div>
  </div>
</div>
<div class="fbtn" style="left:530px;top:2754px">More <svg width="12" height="10" viewBox="0 0 12 10"><path d="M1 9C2 4 5 3 9 3M7 1l3 2-3 2" stroke="#fff" stroke-width="2" fill="none"/></svg></div>

<div class="fcol" style="left:620px">
  <h6>FROM OUR BLOG</h6>
  <ul class="blog">
    <li>› Lorem ipsum dolor sit amet</li>
    <li>› Adipiscing elit, sed do</li>
    <li>› Adipiscing elit, sed do</li>
    <li>› Incididunt ut labore et dolore</li>
    <li>› Quis nostrud exercitation</li>
  </ul>
</div>

<div class="fcol" style="left:788px;font-size:10px;line-height:13px">
  <h6>CONTACT</h6>
  <p style="padding-left:12px">40-46 Marlow Quay, Harbourside<br>London SE1 9XZ</p>
  <p style="margin-top:6px">✉ stay@restwellharbourside.co.uk</p>
  <p style="margin-top:8px">☏ + 44 (0) 20 7946 0456<br>&nbsp;&nbsp;&nbsp;Fax + 44 (0) 20 7946 0789</p>
</div>

<div class="abs bottom">Copyright 2013 Restwell Harbourside UK
  <div class="social"><span class="dot"></span><span class="dot"></span><span class="dot"></span></div>
</div>

</body>
</html>
```